Pelton|Marsh & Quillan business card contest

We need a logo for an upscale boutique diversified company involved in real estate, investments, cattle, and more. Our businesses DO NOT need to be reflected in the business card nor do we want them noted. This is our logo and colors and we love our logo and colors. Our logo looks best against a black background and we like to include the firm name in our logo usage. importantly, the names Pelton and Marsh are separated by | not / and we use an ampersand not the word and.
On the front of the card, we want to include:
company logo and name (Pelton|Marsh & Quillan)
on the back, we would definitely include:
address, email, cell #
logo and name (smaller size than front)

The variable will be location of individual name and title (mine for example is ) - whether on the front OR on the back. interested in variations from which to choose
Dr. Neil R. Whitcombe, CFA
Scientifique des Fusées Financières

we would like to use contemporary symbols for address, email address, cell # with an option for web site that we do not intend to use initially. we like two sided cards and believe this design should use four rounded corners with the standard size. we prefer thicker card stock and may look at metal.

```html
<!DOCTYPE html>
<html lang="en">
<head>
<meta charset="utf-8">
<title>Pelton|Marsh &amp; Quillan — Business Card</title>
<link href="https://fonts.googleapis.com/css2?family=Arimo:wght@400;700&family=Open+Sans:wght@300;400&display=swap" rel="stylesheet">
<style>
  :root {
    --page: #ffffff;
    --ink-black: #000000;
    --brand-orange: #ec8a27;
    --brand-grey: #5e5e5e;
    --logo-grey: #6a6a6a;
    --text-grey: #606060;
    --card-border: #cfcfcf;
    --shadow: #e2e2e2;
    --band-text: #ffffff;
  }
  * { margin: 0; padding: 0; box-sizing: border-box; }
  html, body {
    width: 1200px; height: 1000px; overflow: hidden;
    background: var(--page);
    font-family: "Arimo", Arial, sans-serif;
  }
  .canvas { position: relative; width: 1200px; height: 1000px; }

  .card-shadow {
    position: absolute; height: 12px; border-radius: 50%;
    background: var(--shadow);
  }
  .card {
    position: absolute; width: 474px; height: 272px;
    border-radius: 40px; overflow: hidden;
  }

  /* Front */
  .card--front { left: 363px; top: 149px; background: var(--ink-black); }
  .front-shadow { left: 400px; top: 414px; width: 400px; }
  .front-mark {
    position: absolute; left: 569px; top: 229px;
    width: 60px; height: 60px; background: var(--brand-orange);
  }
  .front-name {
    position: absolute; left: 363px; top: 312px; width: 474px;
    text-align: center; font-size: 24px; font-weight: 400;
    color: var(--logo-grey); letter-spacing: 0.2px;
  }

  /* Back */
  .card--back {
    left: 362px; top: 519px; width: 476px; height: 274px;
    background: var(--page); border: 1px solid var(--card-border);
  }
  .back-shadow { left: 400px; top: 788px; width: 400px; }
  .holder-name {
    position: absolute; left: 29px; top: 41px;
    font-size: 19px; font-weight: 700; letter-spacing: -0.6px;
    color: var(--brand-orange);
  }
  .holder-credential {
    position: absolute; left: 29px; top: 68px;
    font-size: 19px; color: var(--text-grey);
  }
  .contact-list {
    position: absolute; left: 32px; top: 146px; list-style: none;
  }
  .contact-item {
    display: flex; align-items: center; height: 18px;
    font-size: 15px; color: var(--text-grey);
  }
  .contact-icon { width: 11px; height: 11px; margin-right: 10px; fill: var(--text-grey); }
  .back-mark {
    position: absolute; left: 347px; top: 84px;
    width: 42px; height: 42px; background: var(--brand-orange);
  }
  .back-name {
    position: absolute; left: 282px; top: 136px; width: 172px;
    text-align: center; font-size: 16px; color: var(--logo-grey);
  }
  .tagline-band {
    position: absolute; left: 0; bottom: 0; width: 100%; height: 38px;
    background: var(--brand-orange);
  }
  .tagline {
    position: absolute; left: 0; top: 10px; width: 100%;
    padding-right: 24px; text-align: center;
    font-family: "Open Sans", Arial, sans-serif; font-weight: 400;
    font-size: 12px; letter-spacing: 1.3px; text-transform: uppercase;
    color: var(--band-text);
  }
</style>
</head>
<body>
<main class="canvas">
  <div class="card-shadow front-shadow"></div>
  <section class="card card--front" aria-label="Card front"></section>
  <div class="front-mark"></div>
  <p class="front-name">Pelton|Marsh &amp; Quillan</p>

  <div class="card-shadow back-shadow"></div>
  <section class="card card--back" aria-label="Card back">
    <h1 class="holder-name">DR. NEIL R. WHITCOMBE</h1>
    <p class="holder-credential">CFA</p>

    <ul class="contact-list">
      <li class="contact-item">
        <svg class="contact-icon" viewBox="0 0 24 24"><path d="M6.6 10.8a15 15 0 0 0 6.6 6.6l2.2-2.2c.3-.3.7-.4 1-.2 1.1.4 2.3.6 3.6.6.6 0 1 .4 1 1V20c0 .6-.4 1-1 1A17 17 0 0 1 3 4c0-.6.4-1 1-1h3.5c.6 0 1 .4 1 1 0 1.3.2 2.5.6 3.6.1.3 0 .7-.2 1z"/></svg>
        999-999-9999
      </li>
      <li class="contact-item">
        <svg class="contact-icon" viewBox="0 0 24 24"><path d="M2 5h20v14H2zm2 2v.4l8 5 8-5V7zm0 2.8V17h16V9.8l-8 5z"/></svg>
        your@mail.com
      </li>
      <li class="contact-item">
        <svg class="contact-icon" viewBox="0 0 24 24"><path d="M12 2a10 10 0 1 0 0 20 10 10 0 0 0 0-20zm6.9 6h-3a15 15 0 0 0-1.3-3.9A8 8 0 0 1 18.9 8zM12 4c.8 1.2 1.5 2.5 1.9 4h-3.8c.4-1.5 1.1-2.8 1.9-4zM4.3 14a8 8 0 0 1 0-4h3.4a16 16 0 0 0 0 4zm.8 2h3a15 15 0 0 0 1.3 3.9A8 8 0 0 1 5.1 16zm3-8h-3a8 8 0 0 1 4.3-3.9A15 15 0 0 0 8.1 8zM12 20c-.8-1.2-1.5-2.5-1.9-4h3.8c-.4 1.5-1.1 2.8-1.9 4zm2.3-6H9.7a14 14 0 0 1 0-4h4.6a14 14 0 0 1 0 4zm.3 5.9a15 15 0 0 0 1.3-3.9h3a8 8 0 0 1-4.3 3.9zm1.7-5.9a16 16 0 0 0 0-4h3.4a8 8 0 0 1 0 4z"/></svg>
        www.yourwebsite.com
      </li>
      <li class="contact-item">
        <svg class="contact-icon" viewBox="0 0 24 24"><path d="M12 2a7 7 0 0 0-7 7c0 5.2 7 13 7 13s7-7.8 7-13a7 7 0 0 0-7-7zm0 9.5A2.5 2.5 0 1 1 12 6.5a2.5 2.5 0 0 1 0 5z"/></svg>
        Location
      </li>
    </ul>

    <div class="back-mark"></div>
    <p class="back-name">Pelton|Marsh &amp; Quillan</p>

    <div class="tagline-band">
      <p class="tagline">Scientifique des Fusées Financières</p>
    </div>
  </section>
</main>
</body>
</html>
```